table invoices in a modern format! (make it fun to look at!!)

Our has invoices that are shown to our clients. This is currently done in a normal table view, but its boring to look at and is not modern.
We would like to have a modern look and feel
it should ABSOLUTLY not be in table form.
Cards, graphs, pictures, whatever... should be fun and almost interactive.

the table file is how it current looks like.
the other two files were "ideas" to have a better representation
IT DOES NOT NEED TO LOOK LIKE THAT if you have a better idea please go for it.

secondary objective, the graphs/cards/whatever you design should be interactive, meaning I can "click on it" to pay a bill, or see more info.

Let me know if there are more questions!

```html
<!DOCTYPE html>
<html lang="en">
<head>
<meta charset="UTF-8">
<title>Invoice Status by Month</title>
<link rel="stylesheet" href="https://fonts.googleapis.com/css2?family=Roboto:wght@400;500;700&display=swap">
<style>
  :root {
    --page-bg: #cccccc;
    --card-bg: #ffffff;
    --title-ink: #5a5a5a;
    --legend-ink: #666666;
    --tick-ink: #666666;
    --ring: #e6e6e6;
    --paid: rgba(255, 99, 132, 0.5);
    --viewed: rgba(255, 159, 64, 0.5);
    --late: rgba(255, 205, 86, 0.5);
    --partial: rgba(75, 192, 192, 0.5);
  }
  * { box-sizing: border-box; margin: 0; padding: 0; }
  html, body {
    width: 900px;
    height: 1200px;
    overflow: hidden;
    background: var(--page-bg);
    font-family: "Roboto", Arial, sans-serif;
  }
  .board { position: relative; width: 900px; height: 1200px; }
  .month-card {
    position: absolute;
    width: 422px;
    height: 572px;
    background: var(--card-bg);
    cursor: pointer;
  }
  .month-card--apr { left: 13px; top: 13px; }
  .month-card--may { left: 463px; top: 13px; }
  .month-card--jun { left: 13px; top: 615px; }
  .month-card--jul { left: 463px; top: 615px; }

  .month-title {
    position: absolute;
    font-size: 88px;
    line-height: 1;
    font-weight: 500;
    color: var(--title-ink);
    letter-spacing: 1px;
  }
  .month-card--apr .month-title { left: 67px; top: 68px; }
  .month-card--may .month-title { left: 49px; top: 68px; }
  .month-card--jun .month-title { left: 56px; top: 76px; }
  .month-card--jul .month-title { left: 62px; top: 76px; }

  .status-legend { position: absolute; list-style: none; }
  .month-card--apr .status-legend { left: 273px; top: 65px; }
  .month-card--may .status-legend { left: 254px; top: 65px; }
  .month-card--jun .status-legend { left: 264px; top: 71px; }
  .month-card--jul .status-legend { left: 262px; top: 70px; }
  .status-legend li {
    display: flex;
    align-items: center;
    height: 22.5px;
    font-size: 16px;
    color: var(--legend-ink);
  }
  .swatch { width: 42px; height: 16px; margin-right: 10px; }
  .swatch--paid { background: var(--paid); }
  .swatch--viewed { background: var(--viewed); }
  .swatch--late { background: var(--late); }
  .swatch--partial { background: var(--partial); }

  .polar-chart { position: absolute; left: 0; top: 0; width: 422px; height: 572px; }
  .polar-chart .ring { fill: none; stroke: var(--ring); stroke-width: 1.5; }
  .polar-chart .slice { stroke: #ffffff; stroke-width: 1.5; }
  .polar-chart .slice:hover { filter: brightness(0.95); }
  .slice--paid { fill: var(--paid); }
  .slice--viewed { fill: var(--viewed); }
  .slice--late { fill: var(--late); }
  .slice--partial { fill: var(--partial); }
  .polar-chart .tick {
    font-family: "Roboto", Arial, sans-serif;
    font-size: 11px;
    fill: var(--tick-ink);
    text-anchor: middle;
    dominant-baseline: middle;
  }
</style>
</head>
<body>
<main class="board">

  <section class="month-card month-card--apr">
    <h2 class="month-title">APR</h2>
    <ul class="status-legend">
      <li><span class="swatch swatch--paid"></span>Paid</li>
      <li><span class="swatch swatch--viewed"></span>Viewed</li>
      <li><span class="swatch swatch--late"></span>Late</li>
      <li><span class="swatch swatch--partial"></span>Partial</li>
    </ul>
    <svg class="polar-chart" viewBox="0 0 422 572" aria-label="April invoices by status">
      <g>
        <circle class="ring" cx="207" cy="354" r="30.9"/>
        <circle class="ring" cx="207" cy="354" r="61.8"/>
        <circle class="ring" cx="207" cy="354" r="92.7"/>
        <circle class="ring" cx="207" cy="354" r="123.6"/>
        <circle class="ring" cx="207" cy="354" r="154.5"/>
      </g>
      <path class="slice slice--paid" d="M207 354 L207 218 A136 136 0 0 1 343 354 Z"/>
      <path class="slice slice--viewed" d="M207 354 L286 354 A79 79 0 0 1 207 433 Z"/>
      <path class="slice slice--late" d="M207 354 L207 399 A45 45 0 0 1 162 354 Z"/>
      <path class="slice slice--partial" d="M207 354 L52.5 354 A154.5 154.5 0 0 1 207 199.5 Z"/>
      <text class="tick" x="207" y="323.1">20</text>
      <text class="tick" x="207" y="292.2">40</text>
      <text class="tick" x="207" y="261.3">60</text>
      <text class="tick" x="207" y="230.4">80</text>
      <text class="tick" x="207" y="199.5">100</text>
    </svg>
  </section>

  <section class="month-card month-card--may">
    <h2 class="month-title">MAY</h2>
    <ul class="status-legend">
      <li><span class="swatch swatch--paid"></span>Paid</li>
      <li><span class="swatch swatch--viewed"></span>Viewed</li>
      <li><span class="swatch swatch--late"></span>Late</li>
      <li><span class="swatch swatch--partial"></span>Partial</li>
    </ul>
    <svg class="polar-chart" viewBox="0 0 422 572" aria-label="May invoices by status">
      <g>
        <circle class="ring" cx="198" cy="354" r="22.07"/>
        <circle class="ring" cx="198" cy="354" r="44.14"/>
        <circle class="ring" cx="198" cy="354" r="66.21"/>
        <circle class="ring" cx="198" cy="354" r="88.29"/>
        <circle class="ring" cx="198" cy="354" r="110.36"/>
        <circle class="ring" cx="198" cy="354" r="132.43"/>
        <circle class="ring" cx="198" cy="354" r="154.5"/>
      </g>
      <path class="slice slice--paid" d="M198 354 L198 288 A66 66 0 0 1 264 354 Z"/>
      <path class="slice slice--viewed" d="M198 354 L306 354 A108 108 0 0 1 198 462 Z"/>
      <path class="slice slice--late" d="M198 354 L198 508.5 A154.5 154.5 0 0 1 43.5 354 Z"/>
      <path class="slice slice--partial" d="M198 354 L123 354 A75 75 0 0 1 198 279 Z"/>
      <text class="tick" x="198" y="331.93">10</text>
      <text class="tick" x="198" y="309.86">20</text>
      <text class="tick" x="198" y="287.79">30</text>
      <text class="tick" x="198" y="265.71">40</text>
      <text class="tick" x="198" y="243.64">50</text>
      <text class="tick" x="198" y="221.57">60</text>
      <text class="tick" x="198" y="199.5">70</text>
    </svg>
  </section>

  <section class="month-card month-card--jun">
    <h2 class="month-title">JUN</h2>
    <ul class="status-legend">
      <li><span class="swatch swatch--paid"></span>Paid</li>
      <li><span class="swatch swatch--viewed"></span>Viewed</li>
      <li><span class="swatch swatch--late"></span>Late</li>
      <li><span class="swatch swatch--partial"></span>Partial</li>
    </ul>
    <svg class="polar-chart" viewBox="0 0 422 572" aria-label="June invoices by status">
      <g>
        <circle class="ring" cx="205.5" cy="355.5" r="19.31"/>
        <circle class="ring" cx="205.5" cy="355.5" r="38.63"/>
        <circle class="ring" cx="205.5" cy="355.5" r="57.94"/>
        <circle class="ring" cx="205.5" cy="355.5" r="77.25"/>
        <circle class="ring" cx="205.5" cy="355.5" r="96.56"/>
        <circle class="ring" cx="205.5" cy="355.5" r="115.88"/>
        <circle class="ring" cx="205.5" cy="355.5" r="135.19"/>
        <circle class="ring" cx="205.5" cy="355.5" r="154.5"/>
      </g>
      <path class="slice slice--paid" d="M205.5 355.5 L205.5 274.5 A81 81 0 0 1 286.5 355.5 Z"/>
      <path class="slice slice--viewed" d="M205.5 355.5 L342 355.5 A136.5 136.5 0 0 1 205.5 492 Z"/>
      <path class="slice slice--late" d="M205.5 355.5 L205.5 447 A91.5 91.5 0 0 1 114 355.5 Z"/>
      <path class="slice slice--partial" d="M205.5 355.5 L109.5 355.5 A96 96 0 0 1 205.5 259.5 Z"/>
      <text class="tick" x="205.5" y="336.19">10</text>
      <text class="tick" x="205.5" y="316.87">20</text>
      <text class="tick" x="205.5" y="297.56">30</text>
      <text class="tick" x="205.5" y="278.25">40</text>
      <text class="tick" x="205.5" y="258.94">50</text>
      <text class="tick" x="205.5" y="239.62">60</text>
      <text class="tick" x="205.5" y="220.31">70</text>
      <text class="tick" x="205.5" y="201">80</text>
    </svg>
  </section>

  <section class="month-card month-card--jul">
    <h2 class="month-title">JUL</h2>
    <ul class="status-legend">
      <li><span class="swatch swatch--paid"></span>Paid</li>
      <li><span class="swatch swatch--viewed"></span>Viewed</li>
      <li><span class="swatch swatch--late"></span>Late</li>
      <li><span class="swatch swatch--partial"></span>Partial</li>
    </ul>
    <svg class="polar-chart" viewBox="0 0 422 572" aria-label="July invoices by status">
      <g>
        <circle class="ring" cx="183" cy="357" r="19.31"/>
        <circle class="ring" cx="183" cy="357" r="38.63"/>
        <circle class="ring" cx="183" cy="357" r="57.94"/>
        <circle class="ring" cx="183" cy="357" r="77.25"/>
        <circle class="ring" cx="183" cy="357" r="96.56"/>
        <circle class="ring" cx="183" cy="357" r="115.88"/>
        <circle class="ring" cx="183" cy="357" r="135.19"/>
        <circle class="ring" cx="183" cy="357" r="154.5"/>
      </g>
      <path class="slice slice--paid" d="M183 357 L183 283.5 A73.5 73.5 0 0 1 256.5 357 Z"/>
      <path class="slice slice--viewed" d="M183 357 L319.5 357 A136.5 136.5 0 0 1 183 493.5 Z"/>
      <path class="slice slice--late" d="M183 357 L183 471 A114 114 0 0 1 69 357 Z"/>
      <path class="slice slice--partial" d="M183 357 L132 357 A51 51 0 0 1 183 306 Z"/>
      <text class="tick" x="183" y="337.69">10</text>
      <text class="tick" x="183" y="318.37">20</text>
      <text class="tick" x="183" y="299.06">30</text>
      <text class="tick" x="183" y="279.75">40</text>
      <text class="tick" x="183" y="260.44">50</text>
      <text class="tick" x="183" y="241.12">60</text>
      <text class="tick" x="183" y="221.81">70</text>
      <text class="tick" x="183" y="202.5">80</text>
    </svg>
  </section>

</main>
</body>
</html>
```